Harbor Keyvault Password Manager WebApp Design

Harbor Keyvault is seeking an expert UI designer to provide a fresh and modern visual appeal for our product. Our inspiration comes from two major tools that have successfully managed to balance functionality and design aesthetics - Nimbus Folio and LockTrellis. We want our application to exude a similar trustworthiness and modernity, through a clean, intuitive and responsive design.
We have established preliminary mockups and would like the designer to work within these parameters while enhancing the overall user experience. The primary tasks will involve innovative and improved designs of the login screen and the password screen, both being crucial touchpoints for our users. The login screen also serves a crucial role in demonstrating how our system works.
Key Elements:
Logo Integration: We are providing the logo for Harbor Keyvault. The design should align with the logo, both in terms of colors and overall aesthetic, to ensure a cohesive brand identity.
Color Palette: The UI design should adhere to the color palette derived from the logo to maintain brand consistency. The design should effectively utilize these colors to highlight important elements and improve user engagement.
Trustworthy and Modern Design: The UI should be professional and trustworthy. It should mirror the look and feel of Nimbus Folio's simplicity and LockTrellis's solid security design, which inspires user confidence.
Adherence to Mockup Boundaries: The existing mockups serve as a guideline for the layout and placement of elements. The design should respect these boundaries while bringing innovation and visual appeal.
Improved Login Screen: The login screen is a key part of the user's journey and should be designed with utmost care. It should be intuitive, easy-to-use, visually engaging, and educative, showcasing how the system operates and encouraging users to sign in with confidence.
Enhanced Password Screen: The password screen, another key user touchpoint, needs improvement. The different types of passwords should be made more visible and intuitive, easing user interaction and enhancing the overall experience.
Prospective designers are encouraged to test our current version available for free at app.harborkeyvault.example to understand the product better and contribute to meaningful design enhancements.
The goal of this project is to provide a visually compelling and user-friendly interface for Harbor Keyvault that inspires user trust, while adhering to the branding elements, including color scheme and logo design. The ideal designer will have a proven track record of creating compelling UI designs that enhance user experience and engagement.
We preferred the design to be in Figma.
Please provide the 3 design so we can evaluate if we like to choice you:
1. Login Page.
2. Passwords View design
3. Single Passwod Page
We need all the pages to be design that are provided as screenshots.
Target Market(s)
Companies
Industry/Entity Type
Security,
Number of Pages Required
5+ page
Font styles to use
Look and feel
Each slider illustrates characteristics of the customer's brand and the style your logo design should communicate.

```html
<!DOCTYPE html>
<html lang="en">
<head>
<meta charset="utf-8">
<title>Harbor Keyvault – Sign in</title>
<link href="https://fonts.googleapis.com/css2?family=Roboto:wght@300;400;500&display=swap" rel="stylesheet">
<style>
:root{
  --ink:#202124;
  --muted:#3c4043;
  --brand-blue:#3367d6;
  --link:#3b6fd4;
  --card:#f4f4f5;
  --line:#e3e3e6;
  --green:#34a853;
  --azure:#3b8cf7;
  --amber:#fbbc05;
  --red:#ea4335;
  --lock:#3b5fd4;
}
*{box-sizing:border-box;margin:0;padding:0}
html,body{width:1200px;height:731px;overflow:hidden;background:#fff;font-family:"Roboto",Arial,sans-serif;color:var(--ink)}
.page{position:relative;width:1200px;height:731px;overflow:hidden}
.topbar{position:absolute;left:0;top:0;width:1200px;height:62px;background:#fff;box-shadow:0 2px 8px rgba(0,0,0,.05);display:flex;align-items:center;padding-left:17px;gap:9px;z-index:2}
.brand-mark{width:26px;height:26px;background:var(--brand-blue);border-radius:4px}
.brand-name{font-size:15px;font-weight:400;color:#5f6368}
.hero-art{position:absolute;left:100px;top:161px;width:344px;height:364px;border-radius:24px;background:radial-gradient(circle at 55% 45%,#fde7a6 0%,#f3f4fb 55%,#ffffff 100%)}
.welcome-card{position:absolute;left:714px;top:149px;width:400px;height:379px;background:var(--card);border-radius:8px;box-shadow:0 30px 40px -20px rgba(0,0,0,.08);padding:34px 34px 0}
.welcome-title{font-size:24px;font-weight:400;color:var(--link);line-height:1;margin-top:2px}
.welcome-copy{margin-top:10px;font-size:14px;font-weight:300;line-height:23px;color:var(--muted)}
.welcome-copy strong{font-weight:400;color:var(--ink)}
.account-button{position:absolute;left:34px;top:133px;width:283px;height:51px;background:#fff;border:1px solid var(--line);border-radius:6px;display:flex;align-items:center;padding:0 10px}
.avatar{width:28px;height:28px;border-radius:50%;background:var(--red);color:#fff;font-size:12px;display:flex;align-items:center;justify-content:center;flex:none}
.account-text{margin-left:11px;line-height:16px}
.account-name{font-size:11px;font-weight:500}
.account-email{font-size:10px;color:var(--muted);display:flex;align-items:center;gap:6px}
.provider-dot{margin-left:auto;width:16px;height:16px;border-radius:50%;background:var(--azure)}
.divider{position:absolute;left:34px;right:34px;top:230px;height:1px;background:var(--line)}
.how-it-works{position:absolute;left:34px;top:276px;display:flex;gap:14px}
.lock-badge{width:34px;height:34px;border-radius:50%;background:#fff;display:flex;align-items:center;justify-content:center;flex:none;margin-top:-8px}
.how-text{font-size:11px;font-weight:300;line-height:17px;color:var(--ink);width:240px}
.pager{position:absolute;left:79px;top:356px;display:flex;align-items:center;gap:5px}
.pager span{width:3px;height:3px;border-radius:50%;background:#bdbdbd}
.pager .active{width:6px;height:6px;background:var(--green)}
.decor{position:absolute;left:0;top:0}
.footer{position:absolute;left:0;top:672px;width:1200px;height:59px;border-top:1px solid var(--line);text-align:center;font-size:10px;line-height:18.5px;padding-top:12px;color:var(--ink)}
.footer a{color:var(--link);text-decoration:none}
</style>
</head>
<body>
<div class="page">
  <header class="topbar">
    <span class="brand-mark"></span>
    <span class="brand-name">Harbor Keyvault</span>
  </header>

  <div class="hero-art" role="img" aria-label="Illustration of a person pointing at a login form with a user avatar, password fields and a security shield with a check mark"></div>

  <svg class="decor" width="1200" height="731" viewBox="0 0 1200 731" aria-hidden="true">
    <polygon points="0,608 64,672 0,672" fill="var(--green)"/>
    <polygon points="1200,507 1109,599 1182,672 1200,672" fill="var(--azure)"/>
    <polygon points="1129,672 1156,645 1182,672" fill="var(--amber)"/>
  </svg>

  <section class="welcome-card">
    <h1 class="welcome-title">Welcome!</h1>
    <p class="welcome-copy">You can <strong>sign in</strong> or <strong>register</strong> from the button below.<br>Please keep in mind how our system works.</p>

    <button class="account-button" type="button">
      <span class="avatar">A</span>
      <span class="account-text">
        <span class="account-name">Sign in as Orchard</span><br>
        <span class="account-email">orchard.team@harborkeyvault.example
          <svg width="10" height="6" viewBox="0 0 10 6"><path d="M1 1l4 4 4-4" fill="none" stroke="#3c4043" stroke-width="1"/></svg>
        </span>
      </span>
      <span class="provider-dot"></span>
    </button>

    <div class="divider"></div>

    <div class="how-it-works">
      <span class="lock-badge">
        <svg width="14" height="18" viewBox="0 0 14 18"><path d="M3.5 8V5.5a3.5 3.5 0 0 1 7 0V8" fill="none" stroke="var(--lock)" stroke-width="1.8"/><rect x="1" y="8" width="12" height="9.5" rx="1.5" fill="var(--lock)"/><circle cx="7" cy="12.3" r="1.4" fill="#fff"/></svg>
      </span>
      <p class="how-text">Your files are encrypted with different keys. They are dynamically aggregated only in your browser.</p>
    </div>

    <div class="pager"><span></span><span class="active"></span><span></span></div>
  </section>

  <footer class="footer">
    By clicking Sign In with Sonder ID, you agree with our <a href="#">Terms and Use</a><br>
    Learn what data we collect and how we handle it in our <a href="#">Privacy Policy</a>
  </footer>
</div>
</body>
</html>
```